New Website for ReBranded Company - CrewBeacon

We have a successful company and website currently but it is a little dated. We have re-branded the company from Harbor Signal Networks to CrewBeacon and have a new logo for the new name. We are looking to build a newer fresher website with the new name. I will need a concept of the home page and one inside page. You can see our current site at https://www.harborsignalnetworks.example and the new site will be https://www.crewbeacon.example .

I also really like the https://www.pathlantern.example/ website. I like ledgerkite.example website. I like the https://skillorbit.example/ website.

See the attached document for layout and some text to use. Use the pictures I attached as opposed to pictures from the old site as much as you can.

Target Market(s)

Business

Industry/Entity Type

Software Service

Number of Pages Required

2 page

Font styles to use
Sans Serif

Requirements
Must have
• Use the colors from my logo. Professional but modern. We want people to feel like our product makes their staff feel safer at work.
Should not have
• Don't use any red or orange (no stop colors).

```html
<!DOCTYPE html>
<html lang="en">
<head>
<meta charset="utf-8">
<title>CrewBeacon – Get Help Fast</title>
<link href="https://fonts.googleapis.com/css2?family=Montserrat:wght@300;400;500;600;700;800&family=Lato:wght@300;400;700&display=swap" rel="stylesheet">
<style>
:root{
  --green:#7ab648;
  --blue:#3096d4;
  --ink:#1a1a1a;
  --text:#444;
  --muted:#666;
  --night:#0b0b0b;
  --mist:#f6f6f6;
  --white:#fff;
}
*{box-sizing:border-box;margin:0;padding:0}
html,body{width:1200px;height:2828px;overflow:hidden}
body{position:relative;background:var(--white);font-family:'Lato',sans-serif;color:var(--text)}
.abs{position:absolute}
.btn{position:absolute;display:flex;align-items:center;justify-content:center;background:var(--green);color:var(--white);font-family:'Montserrat',sans-serif;font-weight:800;font-size:11px;letter-spacing:.2px;text-transform:uppercase;text-decoration:none}
.brand{display:flex;align-items:center;gap:8px;font-family:'Montserrat',sans-serif;font-weight:600;color:var(--blue)}
.brand-dot{border-radius:50%;background:var(--blue)}

/* nav */
.site-nav{top:0;left:0;width:1200px;height:52px;background:var(--white)}
.site-nav .brand{position:absolute;left:195px;top:12px;font-size:19px}
.site-nav .brand-dot{width:28px;height:28px}
.nav-link{position:absolute;top:21px;font-family:'Montserrat',sans-serif;font-size:10px;font-weight:500;color:#333;letter-spacing:.3px}
.nav-cta{left:870px;top:17px;width:134px;height:20px;font-size:9.5px;font-weight:600}

/* hero */
.hero{top:52px;left:0;width:1200px;height:557px;background:var(--night);overflow:hidden}
.hero-photo{position:absolute;left:500px;top:0;width:700px;height:557px;background:linear-gradient(120deg,#2c3440 0%,#2a4a78 35%,#1f3a63 60%,#6b6f73 85%,#9a9a98 100%);clip-path:polygon(120px 0,700px 0,700px 557px,0 557px,20px 300px)}
.hero h1{position:absolute;left:201px;top:113px;font-family:'Montserrat',sans-serif;font-weight:800;font-size:31px;line-height:36px;color:var(--white);text-transform:uppercase}
.hero p{position:absolute;left:200px;top:232px;font-family:'Montserrat',sans-serif;font-weight:400;font-size:25px;line-height:30px;color:var(--white);width:275px}
.hero .btn{left:201px;top:362px;width:185px;height:34px}

/* feature cards */
.mist{top:609px;left:0;width:1200px;height:444px;background:var(--mist)}
.card{position:absolute;top:525px;height:149px;background:var(--white);box-shadow:0 8px 24px rgba(0,0,0,.08);display:flex;flex-direction:column;align-items:center;padding-top:16px;text-align:center;font-size:13.5px;line-height:16px;color:#555}
.card .mark{width:34px;height:34px;border-radius:50%;background:var(--blue);margin-bottom:18px}
.card-left{left:195px;width:296px}
.card-mid{left:491px;top:519px;width:229px;height:162px;background:var(--blue);color:var(--white);z-index:2}
.card-mid .mark{background:var(--white)}
.card-right{left:720px;width:285px}

/* problem */
.problem{top:760px;left:0;width:1200px;text-align:center}
.problem h2{font-family:'Montserrat',sans-serif;font-weight:400;font-size:34px;line-height:41px;color:var(--ink)}
.problem .lead{font-family:'Lato',sans-serif;font-weight:300;font-size:26px;color:var(--green);margin-top:12px}
.problem .sub{font-family:'Lato',sans-serif;font-weight:300;font-size:25px;color:#333;margin-top:4px}
.problem-cta{left:508px;top:950px;width:185px;height:34px}

/* why */
.why-title{top:1113px;left:0;width:1200px;text-align:center;font-family:'Montserrat',sans-serif;font-weight:400;font-size:34px;color:var(--ink)}
.why-col{position:absolute;top:1194px;width:250px;text-align:center}
.why-col svg{display:block;margin:0 auto 12px}
.why-col h3{font-family:'Montserrat',sans-serif;font-size:11.5px;font-weight:500;color:#333;text-transform:uppercase;margin-bottom:8px}
.why-col p{font-size:10.5px;line-height:17px;color:#555;padding:0 12px}
.why-col .hint{color:var(--blue);font-size:12px;margin-bottom:10px}
.opt-grid{display:grid;grid-template-columns:72px 72px;gap:4px 0;justify-content:center;text-align:left;font-size:10px;color:#555}
.opt-grid span::before{content:"";display:inline-block;width:7px;height:7px;border-radius:50%;background:var(--green);margin-right:4px;vertical-align:0}
.divider{position:absolute;top:1194px;width:1px;height:174px;background:#e3e3e3}
.why-cta{left:508px;top:1408px;width:185px;height:34px}

/* reassurance */
.reassure{top:1533px;left:0;width:585px;height:403px;background:var(--blue)}
.reassure h2{position:absolute;left:195px;top:124px;font-family:'Montserrat',sans-serif;font-weight:700;font-size:30px;line-height:36px;color:var(--white)}
.reassure .btn{left:196px;top:267px;width:129px;height:34px}
.accent-bar{left:572px;top:1598px;width:38px;height:274px;background:var(--green)}
.reach{left:642px;top:1647px;width:340px;font-family:'Montserrat',sans-serif;font-size:23px;line-height:30px;color:var(--ink)}
.stat{position:absolute;top:1764px;height:49px;display:flex;align-items:center;justify-content:center;font-family:'Montserrat',sans-serif;font-size:20px;color:var(--white)}
.stat-states{left:642px;width:112px;background:var(--blue)}
.stat-countries{left:838px;width:139px;background:var(--green)}
.stat-join{left:765px;top:1780px;font-family:'Montserrat',sans-serif;font-size:15px;color:#333}

/* plan */
.plan-title{top:1995px;left:0;width:1200px;text-align:center;font-family:'Montserrat',sans-serif;font-weight:400;font-size:34px;color:var(--ink)}
.step-num{position:absolute;top:2083px;width:83px;height:83px;border-radius:50%;display:flex;align-items:center;justify-content:center;font-family:'Montserrat',sans-serif;font-weight:300;font-size:44px;color:var(--white)}
.step-num.green{background:var(--green)}
.step-num.blue{background:var(--blue)}
.step{position:absolute;top:2085px;width:190px}
.step h4{font-family:'Montserrat',sans-serif;font-weight:500;font-size:11px;line-height:13px;color:#333;text-transform:uppercase;margin-bottom:6px}
.step li{list-style:none;font-size:9.5px;line-height:17px;color:#555}
.step li::before{content:"";display:inline-block;width:7px;height:7px;border-radius:50%;background:var(--green);margin-right:4px}
.step p{font-size:9.5px;line-height:13px;color:#555}
.plan-cta{left:536px;top:2216px;width:129px;height:34px}

/* crisis band */
.band{top:2320px;left:0;width:1200px;height:202px;background:var(--green);text-align:center}
.band h2{padding-top:38px;font-family:'Montserrat',sans-serif;font-weight:700;font-size:30px;line-height:36px;color:var(--white)}
.band .btn{position:absolute;left:549px;top:126px;width:129px;height:34px;background:var(--white);color:var(--green)}

/* footer */
.footer-col{position:absolute;top:2572px}
.footer-col h5{font-family:'Montserrat',sans-serif;font-weight:400;font-size:18px;color:var(--ink);margin-bottom:20px}
.footer-col li{list-style:none;font-size:10.5px;line-height:22.5px;color:#555}
.footer-about{left:195px;width:280px}
.footer-about p{font-size:10.5px;line-height:17.5px;color:#555;width:270px}
.footer-about .brand{margin-top:26px;font-size:30px;font-weight:500}
.footer-about .brand-dot{width:56px;height:56px}
.copyright{left:195px;top:2797px;font-size:9.5px;color:var(--green)}
</style>
</head>
<body>

<header class="abs site-nav">
  <div class="brand"><span class="brand-dot"></span>CrewBeacon</div>
  <span class="nav-link" style="left:647px">HOME</span>
  <span class="nav-link" style="left:700px">BUY ADDONS</span>
  <span class="nav-link" style="left:787px">CUST LOGIN</span>
  <a class="btn nav-cta" href="#">Explore Your Choices</a>
</header>

<section class="abs hero">
  <div class="hero-photo" role="img" aria-label="Close-up of a hand sliding a compact panic button into a jeans pocket"></div>
  <h1>Feel confident<br>that your staff<br>is protected</h1>
  <p>Get a revolutionary new electronic panic button</p>
  <a class="btn" href="#">Ready to get started</a>
</section>

<div class="abs mist"></div>

<div class="card card-left"><span class="mark"></span>Problems Stopped Before<br>They Start For Any Type Of<br>Organization</div>
<div class="card card-mid"><span class="mark"></span>Affordable Prices Starting at<br>$18 per month. No Contracts.<br>No Hidden Costs.</div>
<div class="card card-right"><span class="mark"></span>Alerts by computer, mobile<br>device, text, phone, email,<br>monitoring and E911</div>

<section class="abs problem">
  <h2>DOES THIS PROBLEM MAKE YOU FEEL<br>FRUSTRATED AND ANXIOUS?</h2>
  <p class="lead">Does this problem make you feel frustrated and anxious?</p>
  <p class="sub">Put a simple solution in their hands</p>
</section>
<a class="btn problem-cta" href="#">Ready to get started</a>

<h2 class="abs why-title">WHY BUSINESSES CHOOSE US</h2>

<div class="why-col" style="left:186px">
  <svg width="34" height="36" viewBox="0 0 34 36" fill="none" stroke="#7ab648" stroke-width="2.4" stroke-linejoin="round" aria-hidden="true"><path d="M8 34 L4 22 Q3 17 7 16 L12 15 L10 6 Q10 3 13 3 Q15 3 16 6 L19 15 L26 16 Q30 17 29 22 L26 34 Z"/><path d="M22 4 Q28 4 30 10"/></svg>
  <h3>Easy to use</h3>
  <p>Press a button and let the right people know you need help and open a chat window letting everyone talk on resolving their problem.</p>
</div>
<div class="divider" style="left:456px"></div>
<div class="why-col" style="left:475px">
  <svg width="40" height="36" viewBox="0 0 40 36" fill="#7ab648" aria-hidden="true"><path d="M10 2 H38 V22 H24 L18 28 V22 H10 Z"/><path d="M2 10 H7 V25 H15 V29 L9 34 V29 H2 Z"/></svg>
  <h3>Communicate the way you want</h3>
  <p class="hint">We give you lots of options:</p>
  <div class="opt-grid"><span>Computer</span><span>Text</span><span>Mobile</span><span>E911</span><span>Email</span><span>Call Center</span><span>Phone call</span></div>
</div>
<div class="divider" style="left:757px"></div>
<div class="why-col" style="left:767px">
  <svg width="30" height="36" viewBox="0 0 30 36" aria-hidden="true"><path d="M15 2 L28 7 V17 Q28 28 15 34 Q2 28 2 17 V7 Z" fill="none" stroke="#7ab648" stroke-width="2.6"/><path d="M15 8 L23 11 V17 Q23 24 15 28 Z" fill="#7ab648"/></svg>
  <h3>Cost effective protection</h3>
  <p>By leveraging your existing network and equipment we can lower your costs to give better options to your staff.</p>
</div>

<a class="btn why-cta" href="#">Ready to get started</a>

<section class="abs reassure">
  <h2>We know how scary<br>it can feel to worry<br>about employee safety.</h2>
  <a class="btn" href="#">Start my demo</a>
</section>
<div class="abs accent-bar"></div>
<p class="abs reach">That’s why we have provided a way for customers to get help to staff effectively in</p>
<div class="stat stat-states">45 States</div>
<span class="abs stat-join">covering</span>
<div class="stat stat-countries">5 Countries</div>

<h2 class="abs plan-title">SIMPLE START PLAN</h2>

<div class="step-num green" style="left:197px">1</div>
<div class="step" style="left:292px">
  <h4>Explore your choices</h4>
  <ul><li>Pricing</li><li>Trial</li><li>Quote</li><li>Hardware</li></ul>
</div>
<div class="step-num blue" style="left:482px">2</div>
<div class="step" style="left:578px">
  <h4>Get setup</h4>
  <ul><li>Input Your Alerts</li><li>Input Your Staff</li><li>Install Our Software</li></ul>
</div>
<div class="step-num green" style="left:719px">3</div>
<div class="step" style="left:816px">
  <h4>Feel confident your staff<br>is protected</h4>
  <p>High Five. You just too a major step to getting rid of the anxiety and frustration this gave you.</p>
</div>

<a class="btn plan-cta" href="#">Start my demo</a>

<section class="abs band">
  <h2>Stay Connected with Staff during a<br>Crisis Situations</h2>
  <a class="btn" href="#">Start my demo</a>
</section>

<footer>
  <div class="footer-col footer-about">
    <h5>CALL US 1 – 800 – 555 – 0142</h5>
    <p>When employees feel alone during a threatening situation, we give them a way to let the right resources know that they need help so you can feel confident that your staff is protected.</p>
    <div class="brand"><span class="brand-dot"></span>CrewBeacon</div>
  </div>
  <div class="footer-col" style="left:538px">
    <h5>SHOP</h5>
    <ul><li>Add Ons</li><li>Start My Demo</li><li>Custom Quote</li><li>Start Trial</li></ul>
  </div>
  <div class="footer-col" style="left:694px">
    <h5>ABOUT</h5>
    <ul><li>Affiliates</li><li>Contact</li><li>Support</li><li>Existing Customers</li><li>Industries</li><li>Blog</li><li>FAQ</li></ul>
  </div>
  <div class="footer-col" style="left:855px">
    <h5>LEGAL</h5>
    <ul><li>Privacy Policy</li><li>Terms of Use</li><li>End User License Agreement</li></ul>
  </div>
  <p class="abs copyright">©CrewBeacon 2020</p>
</footer>

</body>
</html>
```